T&R Custom Homes and Remodeling Flyer

We need a new double sided flyer that showcases our service.
Our website is http://trhomesbuildco.example/
Please use the information on http://trhomesbuildco.example/about-us/ for the information in the flyer.
This handout will be used to give to our potential customers and needs to show the complete story of who we are and the services we provide. I have also attached pictures of project we have completed that should be used for the flyer.
Any other pictures can be taken from our photo gallery on the website.

Target Market(s)

Clients who want a custom home or remodel

Industry/Entity Type

Construction

Font styles to use
Serif

Requirements
Must have
• Prominent logo
• Pictures of completed projects
• Tri-fold design- eps file is attached for this
Nice to have
• Manly colors
• If you can find a tasteful way to add the picture of the owners that is great, but it should be small and is not necessary.
Should not have
• Pink/girly touches

```html
<!DOCTYPE html>
<html lang="en">
<head>
<meta charset="utf-8">
<title>T&amp;R Custom Homes and Remodeling – Tri-fold Flyer</title>
<link href="https://fonts.googleapis.com/css2?family=Tinos:wght@400;700&display=swap" rel="stylesheet">
<style>
  :root{
    --stage:#8b8c8f;
    --charcoal:#2b2d31;
    --charcoal-deep:#222428;
    --navy:#1c2b4d;
    --accent-blue:#2385c9;
    --text-light:#e3e4e6;
    --silver-hi:#f4f5f6;
    --silver-lo:#c9ccd0;
    --rule:#1c2b4d;
  }
  *{box-sizing:border-box;margin:0;padding:0}
  html,body{width:1200px;height:1200px;overflow:hidden}
  body{background:var(--stage);font-family:"Tinos","Times New Roman",serif;position:relative}
  .sheet{position:absolute;left:30px;width:1140px;height:540px;display:flex;box-shadow:0 6px 18px rgba(0,0,0,.35);overflow:hidden}
  .sheet--outside{top:40px}
  .sheet--inside{top:620px}
  .panel{position:relative;width:380px;height:100%;overflow:hidden}
  .panel + .panel{border-left:1px solid rgba(0,0,0,.25)}
  .photo{position:absolute}
  .base-band{position:absolute;left:0;right:0;bottom:0;height:12px;background:var(--navy)}

  /* outside */
  .flap{background:var(--charcoal)}
  .photo-caption{position:absolute;right:10px;color:#fff;font-weight:700;font-size:20px;letter-spacing:.5px;text-shadow:0 1px 3px #000}
  .back{background:var(--charcoal)}
  .back-copy{position:absolute;top:172px;left:28px;right:28px;color:var(--text-light)}
  .headline{color:var(--accent-blue);font-size:20px;line-height:1.2;margin-bottom:12px}
  .intro{font-size:14px;line-height:1.35}
  .contact{margin-top:14px;text-align:center;font-size:14px;line-height:1.35}
  .contact .mark{display:inline-block;width:12px;height:12px;background:var(--accent-blue);margin-bottom:4px}
  .contact .person{color:var(--accent-blue)}
  .owners{position:absolute;left:115px;bottom:18px;width:150px;height:64px}
  .cover{background:linear-gradient(160deg,var(--silver-hi),var(--silver-lo))}
  .logo{position:absolute;top:60px;left:0;right:0;text-align:center;color:var(--navy)}
  .logo .square{display:inline-block;width:22px;height:22px;background:var(--navy);margin-bottom:12px}
  .logo .name{font-weight:700;font-size:30px;line-height:1.15;padding:0 30px}
  .cover-photo{left:0;right:0;top:205px;bottom:12px}

  /* inside */
  .about{background:var(--charcoal)}
  .section-bar{position:absolute;top:22px;left:18px;right:18px;height:26px;background:var(--navy);color:#fff;font-size:15px;padding:4px 10px}
  .body-copy{color:var(--text-light);font-size:12.5px;line-height:1.38;text-align:justify}
  .about .body-copy{position:absolute;top:58px;left:22px;right:22px}
  .about .body-copy p + p{margin-top:7px}
  .middle{background:var(--charcoal)}
  .middle .body-copy{position:absolute;top:24px;left:22px;right:22px}
  .middle .body-copy p + p{margin-top:7px}
  .services-title{color:var(--accent-blue);font-size:15px;margin-top:10px}
  .services{display:grid;grid-template-columns:1fr 1fr;list-style:none;margin-top:4px}
  .services li{font-size:14px;color:var(--text-light);padding-left:14px;position:relative}
  .services li::before{content:"";position:absolute;left:2px;top:7px;width:5px;height:5px;border-radius:50%;background:var(--accent-blue)}
</style>
</head>
<body>

<section class="sheet sheet--outside" aria-label="Flyer outside">
  <div class="panel flap">
    <div class="photo" role="img" aria-label="Completed house exterior with brick and a railed balcony" style="left:0;top:0;width:380px;height:160px;background:linear-gradient(180deg,#a9afb6,#6f5d54)"></div>
    <div class="photo" role="img" aria-label="Stone front porch with columns after remodel" style="left:0;top:164px;width:380px;height:186px;background:linear-gradient(160deg,#b7aa95,#6d6156)"></div>
    <span class="photo-caption" style="top:318px">AFTER</span>
    <div class="photo" role="img" aria-label="Front entrance before remodel" style="left:0;top:354px;width:380px;height:174px;background:linear-gradient(160deg,#a39b91,#4f4640)"></div>
    <span class="photo-caption" style="top:492px">BEFORE</span>
    <div class="base-band"></div>
  </div>

  <div class="panel back">
    <div class="photo" role="img" aria-label="Balcony with wood railing and brick wall" style="left:0;top:0;width:380px;height:150px;background:linear-gradient(180deg,#b3b6ba,#5e4a42)"></div>
    <div class="back-copy">
      <p class="headline">Planning your dream home, remodeling your current one, or doing a simple addition?</p>
      <p class="intro">T&amp;R specializes in custom home building and remodeling. Our construction team is here to cover your every need.</p>
      <div class="contact">
        <span class="mark"></span><br>
        T &amp; R Homes LLC<br>
        1840 Fieldstone Avenue Suite 210<br>
        Millbrook, IL 60500<br>
        <span class="person">Dan Reyes:</span> 555-014-2287<br>
        <span class="person">Mark Tolliver:</span> 555-013-9640
      </div>
    </div>
    <div class="photo owners" role="img" aria-label="Small photo of the two company owners" style="background:linear-gradient(180deg,#d9d6d0,#3a3a3c)"></div>
    <div class="base-band"></div>
  </div>

  <div class="panel cover">
    <div class="logo">
      <span class="square"></span>
      <p class="name">T&amp;R Custom Homes and Remodeling</p>
    </div>
    <svg width="380" height="60" viewBox="0 0 380 60" style="position:absolute;top:172px;left:0" aria-hidden="true">
      <path d="M0 50 Q190 10 380 18 L380 60 L0 60 Z" fill="#8a8f94"/>
      <path d="M0 44 Q190 4 380 12" fill="none" stroke="var(--rule)" stroke-width="4"/>
    </svg>
    <div class="photo cover-photo" role="img" aria-label="Arched mahogany double front door framed by white columns" style="background:linear-gradient(180deg,#8c8f93 0%,#6a3a2c 45%,#5b2a20 70%,#8c6c57 100%)"></div>
    <div class="base-band"></div>
  </div>
</section>

<section class="sheet sheet--inside" aria-label="Flyer inside">
  <div class="panel about">
    <div class="section-bar">About T&amp;R</div>
    <div class="body-copy">
      <p>With more than 20 years combined experience in construction, T&amp;R maintains the absolute highest levels of quality, material, workmanship and service in each and every project we build.</p>
      <p>A reputation is only as great as the last referral and we understand that the future of our business relies upon satisfied customers. We take the time to fully understand our customer's expectations. Customer service is more than just a trendy marketing theme, it is the underlying philosophy in everything we do and our home buyers reap the benefits of this philosophy.</p>
      <p>T&amp;R is committed to building quality homes with meticulous craftsmanship, custom designs, and thoughtful touches that add to the homeowners' quality of life. Over the years, we have developed close working relationships with some of the best local craftsmen, vendors, and suppliers located in the western suburbs of Chicago.</p>
    </div>
    <div class="photo" role="img" aria-label="Bathroom vanity with mosaic tile wall" style="left:0;top:392px;width:380px;height:148px;background:linear-gradient(160deg,#6f6a63,#2a2624)"></div>
  </div>

  <div class="panel middle">
    <div class="body-copy">
      <p>These trade partners know we expect only the highest level of craftsmanship and they are required to perform at only the highest standards of professionalism, accuracy and timeliness. We take pride in creating homes that are as beautiful to look at, as they are comfortable to live in.</p>
      <p>Throughout our experience we have developed lasting values of honesty, real quality, attention to fine detail, efficiency, timeliness, and most of all how to meet a customer's expectation by asking the right questions. With these principles, character and dedication we are able to do things right the first time.</p>
      <p class="services-title">We can serve you constructing:</p>
      <ul class="services">
        <li>Front door</li><li>Foyer</li>
        <li>Kitchen</li><li>Bathroom</li>
      </ul>
    </div>
    <div class="photo" role="img" aria-label="Bathroom with dark wood cabinets and tile floor" style="left:0;top:392px;width:190px;height:148px;background:linear-gradient(160deg,#8a7a66,#3a2a20)"></div>
    <div class="photo" role="img" aria-label="Kitchen with blue walls and tray ceiling" style="left:192px;top:392px;width:188px;height:148px;background:linear-gradient(160deg,#d8d4cc,#1f3a7a 60%,#4a2e22)"></div>
  </div>

  <div class="panel">
    <div class="photo" role="img" aria-label="Foyer with arched doorway and hardwood floor" style="left:0;top:0;width:380px;height:176px;background:linear-gradient(160deg,#d6d0c4,#5a3c2a)"></div>
    <div class="photo" role="img" aria-label="Kitchen with cherry cabinets and window bay" style="left:0;top:180px;width:380px;height:178px;background:linear-gradient(160deg,#c9c2b2,#7a3a1e)"></div>
    <div class="photo" role="img" aria-label="Open kitchen with white island and dark cabinetry" style="left:0;top:362px;width:380px;height:178px;background:linear-gradient(160deg,#bdb7ad,#3c2a22)"></div>
  </div>
</section>

</body>
</html>
```